Phuket Thailand - Rental Villa Website

I have a villa for rent in Thailand and require a website - i need to demo pictures/walk through video, local attractions, villa facilities description plus seaonal rates and online booking.

Industry/Entity Type

Rental

Coding

Coded - Design and coding required

```html
<!DOCTYPE html>
<html lang="en">
<head>
<meta charset="utf-8">
<title>Kamala Bay Villa</title>
<link rel="stylesheet" href="https://fonts.googleapis.com/css2?family=Cinzel:wght@400;700&family=Open+Sans:wght@400;600&family=Arimo&display=swap">
<style>
:root{
  --sand:#e2c99f;
  --sand-light:#e8d2a8;
  --cocoa:#241509;
  --cocoa-mid:#3a2818;
  --taupe:#6e6050;
  --taupe-light:#877868;
  --teal:#0e6e99;
  --white:#ffffff;
  --rule:#d9cfc3;
  --black:#000000;
  --lake:#5a9cb8;
  --lake-light:#9cc4d2;
}
*{box-sizing:border-box;margin:0;padding:0}
html,body{width:1003px;height:1200px;overflow:hidden;background:var(--sand)}
body{position:relative;font-family:"Open Sans",sans-serif;color:var(--white)}
.abs{position:absolute}
.btn{position:absolute;display:flex;align-items:center;justify-content:center;background:var(--teal);color:var(--white);border-radius:13px;font-size:11px;letter-spacing:-.2px;height:25px;text-decoration:none}
.header{left:29px;top:29px;width:943px;height:97px;background:var(--cocoa)}
.brand{left:35px;top:22px;font-family:"Cinzel",serif;font-weight:400;font-size:26px;line-height:1;color:var(--white);display:flex;align-items:center;gap:10px;white-space:nowrap}
.brand-dot{width:12px;height:12px;border-radius:50%;background:var(--teal)}
.brand small{display:block;font-size:11px;letter-spacing:6px;margin-top:6px}
.nav{left:29px;top:126px;width:943px;height:44px;background:var(--taupe);border-top:1px solid var(--taupe-light)}
.nav a{position:absolute;top:11px;height:25px;border-radius:13px;background:var(--cocoa-mid);color:var(--white);font-size:11px;display:flex;align-items:center;justify-content:center;text-decoration:none;letter-spacing:-.3px;white-space:nowrap}
.nav a.active{background:var(--sand-light);color:var(--cocoa)}
.strip{left:29px;top:170px;width:943px;height:7px;background:var(--cocoa)}
.hero{left:29px;top:177px;width:943px;height:372px;background:linear-gradient(180deg,var(--lake-light) 0%,var(--lake) 55%,var(--lake-light) 100%)}
.caption{left:29px;top:498px;width:943px;height:51px;background:rgba(22,34,44,.88);font-family:"Cinzel",serif;font-size:17px;display:flex;align-items:center;justify-content:center;white-space:nowrap}
.hero-base{left:29px;top:549px;width:943px;height:50px;background:var(--cocoa)}
.feature-box{left:604px;top:203px;width:356px;height:268px;background:rgba(68,52,38,.95);border:4px solid var(--sand-light)}
.feature-box h1{font-family:"Cinzel",serif;font-weight:400;font-size:30px;text-align:center;margin-top:16px;white-space:nowrap}
.rule{position:absolute;height:1px;background:var(--rule)}
.copy{position:absolute;font-size:11.5px;line-height:15.8px}
.photo{position:absolute}
.features{left:29px;top:611px;width:943px;height:330px;background:radial-gradient(ellipse at center,#ffffff 30%,#e4e4e4 100%)}
.card{position:absolute;top:26px;width:301px;height:278px;background:var(--cocoa);border:4px solid var(--sand-light)}
.card h2{position:absolute;left:8px;top:6px;width:277px;height:40px;background:linear-gradient(90deg,var(--taupe),var(--taupe-light));font-family:"Cinzel",serif;font-weight:400;font-size:27px;text-align:center;line-height:42px;white-space:nowrap}
.footer{left:29px;top:953px;width:946px;height:160px;background:var(--cocoa)}
.col{position:absolute;top:22px;width:190px}
.col h3{font-family:"Cinzel",serif;font-weight:400;font-size:15px;padding-left:15px;padding-bottom:8px;border-bottom:2px solid var(--taupe-light);white-space:nowrap}
.col ul{list-style:none;padding:12px 0 0 15px;font-family:"Arimo",sans-serif;font-size:13.5px;line-height:25px;white-space:nowrap}
.bar{left:29px;top:1112px;width:946px;height:55px;background:var(--black)}
.bar .brand-sm{left:22px;top:17px;font-family:"Cinzel",serif;font-size:15px;color:var(--white);white-space:nowrap}
.bar nav a{position:absolute;top:22px;font-size:11px;color:#d8d8d8;text-decoration:none;letter-spacing:-.2px;white-space:nowrap}
.social{position:absolute;top:14px;width:26px;height:26px;border-radius:50%;background:var(--sand-light)}
</style>
</head>
<body>
<header class="abs header">
  <div class="abs brand"><span class="brand-dot"></span><div>Kamala Bay Villa<small>RENTAL VILLA</small></div></div>
  <a class="btn" style="left:788px;top:39px;width:85px">BOOK NOW</a>
</header>
<nav class="abs nav">
  <a class="active" style="left:67px;width:81px">HOME</a>
  <a style="left:179px;width:113px">ABOUT THE VILLA</a>
  <a style="left:319px;width:99px">VIRTUAL TOUR</a>
  <a style="left:445px;width:81px">PRICING</a>
  <a style="left:561px;width:86px">AVAILABILITY</a>
  <a style="left:672px;width:80px">REVIEWS</a>
  <a style="left:788px;width:80px">CONTACT</a>
</nav>
<div class="abs strip"></div>
<div class="abs hero" role="img" aria-label="Infinity pool terrace overlooking a lake with palm trees and hills"></div>
<div class="abs caption">Wonderful Vacation Villa In The Most Sought-after Location By Tourists</div>
<div class="abs hero-base"></div>
<section class="abs feature-box">
  <h1>Vacation Villa</h1>
  <div class="rule" style="left:20px;top:63px;width:308px"></div>
  <div class="photo" role="img" aria-label="Villa bedroom interior" style="left:20px;top:79px;width:150px;height:118px;background:linear-gradient(135deg,#8a7a66,#b9ae9c 55%,#6a5a48)"></div>
  <p class="copy" style="left:183px;top:76px;width:158px">lorem ipsum dolor sit amet consectetur und adipiscing elit sit amet lorem ipsum dolor sit amet consectetur und adipiscing elit sit amet ipsum lorem adipiscing sit consectetur elit.</p>
  <div class="rule" style="left:20px;top:212px;width:308px"></div>
  <a class="btn" style="left:119px;top:231px;width:118px">VIEW DETAILS</a>
</section>
<section class="abs features">
  <article class="card" style="left:15px">
    <h2>Location</h2>
    <div class="rule" style="left:10px;top:60px;width:275px"></div>
    <div class="photo" role="img" aria-label="Villa exterior with tiled roof and garden" style="left:8px;top:76px;width:130px;height:121px;background:linear-gradient(135deg,#7e8078,#6a5244)"></div>
    <p class="copy" style="left:146px;top:72px;width:140px">lorem ipsum dolor sit amet consectetur und adipiscing elit sit amet lorem ipsum dolor sit amet consectetur und elit sit amet ipsum sit elit. ipsum lorem</p>
    <div class="rule" style="left:10px;top:221px;width:275px"></div>
    <a class="btn" style="left:88px;top:237px;width:118px">VIEW DETAILS</a>
  </article>
  <article class="card" style="left:322px">
    <h2>Amenities</h2>
    <div class="rule" style="left:10px;top:60px;width:275px"></div>
    <div class="photo" role="img" aria-label="Swimming pool with turquoise tiles" style="left:8px;top:76px;width:130px;height:121px;background:linear-gradient(180deg,#7fa8a2,#237a6e)"></div>
    <p class="copy" style="left:146px;top:72px;width:140px">lorem ipsum dolor sit amet consectetur und adipiscing elit sit amet lorem ipsum dolor sit amet consectetur und adipiscing elit sit amet sit consectetur elit.</p>
    <div class="rule" style="left:10px;top:221px;width:275px"></div>
    <a class="btn" style="left:88px;top:237px;width:118px">VIEW DETAILS</a>
  </article>
  <article class="card" style="left:628px">
    <h2>Entertainment</h2>
    <div class="rule" style="left:10px;top:60px;width:275px"></div>
    <div class="photo" role="img" aria-label="Neon-lit nightlife street at night" style="left:8px;top:76px;width:130px;height:121px;background:linear-gradient(135deg,#2a1a40,#9a3a2a 60%,#b08030)"></div>
    <p class="copy" style="left:146px;top:72px;width:140px">lorem ipsum dolor sit amet consectetur und adipiscing elit sit amet lorem ipsum dolor und adipiscing elit sit amet lorem adipiscing sit consectetur.</p>
    <div class="rule" style="left:10px;top:221px;width:275px"></div>
    <a class="btn" style="left:88px;top:237px;width:118px">VIEW DETAILS</a>
  </article>
</section>
<footer class="abs footer">
  <div class="col" style="left:47px"><h3>ABOUT THE CITY</h3><ul><li>General Information</li><li>Important Numbers</li></ul></div>
  <div class="col" style="left:274px"><h3>THINGS TO DO</h3><ul><li>Where to go</li><li>Nightlife &amp; Entertainment</li></ul></div>
  <div class="col" style="left:500px"><h3>RESTAURANTS &amp; BARS</h3><ul><li>Restaurants</li><li>Bars &amp; Nightclubs</li></ul></div>
  <div class="col" style="left:736px;width:180px"><h3>CONTACT US</h3><ul><li>Friendbook</li><li>Chirper</li><li>Email us</li></ul></div>
</footer>
<div class="abs bar">
  <div class="abs brand-sm">Kamala Bay Villa</div>
  <nav>
    <a style="left:207px">HOME</a>
    <a style="left:264px">ABOUT THE VILLA</a>
    <a style="left:375px">VIRTUAL TOUR</a>
    <a style="left:471px">PRICING</a>
    <a style="left:536px">AVAILABILITY</a>
    <a style="left:626px">REVIEWS</a>
    <a style="left:696px">CONTACT</a>
  </nav>
  <span class="social" style="left:791px" aria-label="Friendbook"></span>
  <span class="social" style="left:840px" aria-label="Chirper"></span>
  <span class="social" style="left:889px" aria-label="Pin board"></span>
</div>
</body>
</html>
```